Ironvale placard

I need a placard designed that will go in my monthly subscription boxes to describe the products inside. There must be space to write 3-5 sentences on each product.
the first area will be titled: For your flowing mane
2 for your macho glow
3 to keep you smelling macho
4 to keep you clanging and banging at the gym.
Placard will be 5inchs wide and 7inchs long

I have attached the logo and the website address must be used in the design ironvalegoods.com.

Target Market(s)

men between 20-50

Colors

Designer to choose colors to be used in the design.

Requirements
Must have
• My website address ironvalegoods.com
• 4 area to write 3-5 sentences
• 1 for your flowing mane
• 2to keep you smelling macho
• 3 to keep you clanging and banging at the gym
• 4 for your macho glow

```html
<!DOCTYPE html>
<html lang="en">
<head>
<meta charset="utf-8">
<title>Ironvale Placard</title>
<link rel="stylesheet" href="https://fonts.googleapis.com/css2?family=Open+Sans:wght@400;600&family=PT+Sans+Narrow:wght@400;700&display=swap">
<style>
  :root {
    --page: #ffffff;
    --card: #2b2929;
    --card-tone: #343131;
    --ink-light: #ffffff;
    --ink-dark: #111111;
    --brand-red: #e31b23;
  }
  * { margin: 0; padding: 0; box-sizing: border-box; }
  html, body {
    width: 1200px; height: 1200px; overflow: hidden;
    background: var(--page);
  }
  .placard {
    position: absolute; left: 171px; top: 0;
    width: 857px; height: 1200px;
    background: radial-gradient(circle at 50% 50%, var(--card-tone), var(--card));
    color: var(--ink-light);
    overflow: hidden;
  }
  .brand-panel {
    position: absolute; left: 275px; top: 0;
    width: 306px; height: 304px;
    background: var(--page);
    display: flex; flex-direction: column; align-items: center; justify-content: flex-end;
    padding-bottom: 24px;
  }
  .brand-mark {
    width: 110px; height: 110px;
    background: var(--brand-red);
    margin-bottom: 30px;
  }
  .brand-name {
    font-family: 'Open Sans', sans-serif;
    font-weight: 600; font-size: 46px; letter-spacing: 3px;
    color: var(--ink-dark); line-height: 1;
    margin-bottom: 14px;
  }
  .brand-tagline {
    font-family: 'PT Sans Narrow', sans-serif;
    font-weight: 700; font-size: 12.5px; text-transform: uppercase;
    color: var(--ink-dark); white-space: nowrap;
  }
  .product {
    position: absolute; left: 47px; width: 762px;
  }
  .product-title {
    font-family: 'Open Sans', sans-serif;
    font-weight: 600; font-size: 27px; line-height: 1.2;
    white-space: nowrap;
  }
  .product-copy {
    margin-left: 33px; margin-top: 4px;
    font-family: 'PT Sans Narrow', sans-serif;
    font-size: 18.6px; line-height: 25.7px;
    text-align: justify; text-align-last: justify;
  }
  .product.mane { top: 345px; }
  .product.scent { top: 531px; }
  .product.gym { top: 717px; }
  .product.gym .product-title { margin-left: 7px; }
  .product.glow { top: 902px; }
  .site-address {
    position: absolute; left: 0; right: 0; top: 1160px;
    text-align: center;
    font-family: 'Open Sans', sans-serif;
    font-size: 28px; line-height: 1.2;
  }
</style>
</head>
<body>
<main class="placard" role="img" aria-label="Dark charcoal card with faint pattern of barber tools, beards, moustaches and gym weights">
  <header class="brand-panel">
    <div class="brand-mark"></div>
    <div class="brand-name">Ironvale</div>
    <div class="brand-tagline">Grooming goods and gear for hardworking gentlemen</div>
  </header>

  <section class="product mane">
    <h2 class="product-title">1. For your flowing mane.</h2>
    <p class="product-copy">Lorem ipsum dolor sit amet, consectetuer adipiscing elit. Aenean commodo ligula eget dolor. Aenean massa. Cum sociis natoque penatibus et magnis dis parturient montes, nascetur ridiculus mus. Donec quam felis, ultricies nec, pellentesque eu, pretium quis, sem. Nulla consequat massa quis enim. Donec pede justo, fringilla vel, aliquet nec, vulputate eget, arcu. In enim justo, rhoncus ut, imperdiet a, venenatis vitae, justo. Nullam dictum felis eu pede mollis pretium. Integer tincidunt.Cras dapibus. Vivamus elementum semper nisi.</p>
  </section>

  <section class="product scent">
    <h2 class="product-title">2. To keep you smelling macho.</h2>
    <p class="product-copy">Lorem ipsum dolor sit amet, consectetuer adipiscing elit. Aenean commodo ligula eget dolor. Aenean massa. Cum sociis natoque penatibus et magnis dis parturient montes, nascetur ridiculus mus. Donec quam felis, ultricies nec, pellentesque eu, pretium quis, sem. Nulla consequat massa quis enim. Donec pede justo, fringilla vel, aliquet nec, vulputate eget, arcu. In enim justo, rhoncus ut, imperdiet a, venenatis vitae, justo. Nullam dictum felis eu pede mollis pretium. Integer tincidunt.Cras dapibus. Vivamus elementum semper nisi.</p>
  </section>

  <section class="product gym">
    <h2 class="product-title">3. To keep you clanging and banging at the gym.</h2>
    <p class="product-copy">Lorem ipsum dolor sit amet, consectetuer adipiscing elit. Aenean commodo ligula eget dolor. Aenean massa. Cum sociis natoque penatibus et magnis dis parturient montes, nascetur ridiculus mus. Donec quam felis, ultricies nec, pellentesque eu, pretium quis, sem. Nulla consequat massa quis enim. Donec pede justo, fringilla vel, aliquet nec, vulputate eget, arcu. In enim justo, rhoncus ut, imperdiet a, venenatis vitae, justo. Nullam dictum felis eu pede mollis pretium. Integer tincidunt.Cras dapibus. Vivamus elementum semper nisi.</p>
  </section>

  <section class="product glow">
    <h2 class="product-title">4. For your macho glow.</h2>
    <p class="product-copy">Lorem ipsum dolor sit amet, consectetuer adipiscing elit. Aenean commodo ligula eget dolor. Aenean massa. Cum sociis natoque penatibus et magnis dis parturient montes, nascetur ridiculus mus. Donec quam felis, ultricies nec, pellentesque eu, pretium quis, sem. Nulla consequat massa quis enim. Donec pede justo, fringilla vel, aliquet nec, vulputate eget, arcu. In enim justo, rhoncus ut, imperdiet a, venenatis vitae, justo. Nullam dictum felis eu pede mollis pretium. Integer tincidunt.Cras dapibus. Vivamus elementum semper nisi.</p>
  </section>

  <footer class="site-address">ironvalegoods.com</footer>
</main>
</body>
</html>
```